Business Card - Existing Logo & Branding copied to Business Card Format

We are looking for a designer to help with designing a two sided business card for us. We sell a web based software platform that helps people sell access to online training.
We have an existing logo and recently completed a design project here on draft hive to have someone design a nice trade show booth for us (also attached file for that design as well as our logo). We really like the look and feel of the tradeshow booth design. The fonts, colors, etc all work for us. We are hoping someone can create something very similar just in business card format.
Should be pretty straight forward hopefully....
On one side we want the logo, employee name, email address, phone and fax. On the other side we would like the text "transform your organizations training, revenue products = revenue" - See the attached PSD for what we want that to look like.
You can also see our website at www.tutorvane.com for an example of our branding.
We are open to ideas, have done several projects on draft hive and love when designers come up with creative approaches that are even better then what we envisioned.
Software

```html
<!DOCTYPE html>
<html lang="en">
<head>
<meta charset="utf-8">
<title>TutorVane – Business Card</title>
<link rel="stylesheet" href="https://fonts.googleapis.com/css2?family=Oswald:wght@600&family=IM+Fell+English+SC&family=Black+Ops+One&family=Nunito:wght@800&display=swap">
<style>
  :root {
    --card-bg: #ffffff;
    --brand-red: #b3232d;
    --ink-dark: #3b3b3d;
    --ink-black: #1c1c1c;
    --on-red: #ffffff;
  }
  * { margin: 0; padding: 0; box-sizing: border-box; }
  html, body { width: 1200px; height: 686px; overflow: hidden; background: var(--card-bg); }
  .card { position: relative; width: 1200px; height: 686px; background: var(--card-bg); }

  .brand { position: absolute; left: 69px; top: 50px; display: flex; align-items: center; gap: 26px; }
  .brand-square { width: 70px; height: 70px; background: var(--brand-red); }
  .brand-name { font-family: "Nunito", sans-serif; font-weight: 800; font-size: 52px; color: var(--ink-dark); letter-spacing: -0.5px; }

  .person-name {
    position: absolute; right: 64px; top: 318px;
    font-family: "Oswald", sans-serif; font-weight: 600; font-size: 132px; line-height: 1;
    letter-spacing: -3px; color: var(--ink-dark); white-space: nowrap;
  }
  .person-name .surname { color: var(--brand-red); }

  .job-title {
    position: absolute; right: 64px; top: 472px;
    font-family: "IM Fell English SC", serif; font-size: 32px; line-height: 1;
    color: var(--ink-black); white-space: nowrap;
  }

  .bar { position: absolute; background: var(--brand-red); height: 52px; }
  .bar-text {
    position: absolute; height: 52px; display: flex; align-items: center;
    font-family: "Nunito", sans-serif; font-weight: 800; font-size: 29px; color: var(--on-red);
    white-space: nowrap;
  }
  .label {
    position: absolute; height: 52px; display: flex; align-items: center; justify-content: center;
    font-family: "Black Ops One", sans-serif; font-size: 40px; color: var(--brand-red);
  }
</style>
</head>
<body>
  <div class="card">
    <div class="brand">
      <span class="brand-square"></span>
      <span class="brand-name">TutorVane</span>
    </div>

    <h1 class="person-name">Alan <span class="surname">Brooks</span></h1>
    <p class="job-title">Chief Executive Officer</p>

    <!-- email row -->
    <div class="bar" style="left:571px; top:519px; width:63px;"></div>
    <div class="label" style="left:644px; top:519px; width:42px;">E</div>
    <div class="bar" style="left:696px; top:519px; width:504px;"></div>
    <div class="bar-text" style="left:718px; top:519px;">info@tutorvane.com</div>

    <!-- fax / phone row -->
    <div class="bar" style="left:441px; top:586px; width:68px;"></div>
    <div class="label" style="left:519px; top:586px; width:41px;">F</div>
    <div class="bar" style="left:574px; top:586px; width:266px;"></div>
    <div class="bar-text" style="left:588px; top:586px;">02 5550 1234</div>
    <div class="label" style="left:855px; top:586px; width:42px;">T</div>
    <div class="bar" style="left:905px; top:586px; width:295px;"></div>
    <div class="bar-text" style="left:925px; top:586px;">0400 555 200</div>
  </div>
</body>
</html>
```